VERDALUX " need somthing eye catching and envirnmental friendely materials

Business Card " UNIQUE..
- use the agreed on logo.
- use wooden background.
- the environmental sound should be HIGH.

Company slogan is ZERO DISCHARGE.
We work in deploying the latest technology “ USA & Europe” in the field of drill cutting recycle and economically managing the footprint.
With the ramp up in oil demands and the increase in oil prices , operators are extending their operations into new geographical areas “ government regulations and eco-sounds” created the need to a specialty services and products that should go parallel or even ahead.

Target Market(s)

OIL field and environmental concerned.
Mainly ENGINEERS.

Industry/Entity Type

Government

Font styles to use
Decorative
Script

Colors

Designer to choose colors to be used in the design.

Requirements
Must have
• Eco - sounded.

```html
<!DOCTYPE html>
<html lang="en">
<head>
<meta charset="utf-8">
<title>VERDALUX Business Card</title>
<link rel="stylesheet" href="https://fonts.googleapis.com/css2?family=Montserrat:wght@700;800&family=Source+Sans+3:wght@400;600&display=swap">
<style>
  :root {
    --green: #1f9a4a;
    --green-dark: #17803c;
    --charcoal: #2f3336;
    --grey-text: #8a8a8a;
    --ink: #2b2b2b;
    --rule: #9a9a9a;
    --card-edge: #c9c9c9;
    --page: #ffffff;
    --wood-light: #e9cfa6;
    --wood-mid: #dcb98a;
    --wood-deep: #cfa874;
  }
  * { box-sizing: border-box; margin: 0; padding: 0; }
  html, body { width: 1039px; height: 1200px; overflow: hidden; background: var(--page); }
  body { position: relative; font-family: "Source Sans 3", sans-serif; }

  .card-front {
    position: absolute; left: 0; top: 0; width: 1039px; height: 584px;
    background: linear-gradient(90deg, var(--wood-mid) 0%, var(--wood-light) 22%, var(--wood-mid) 45%, var(--wood-light) 70%, var(--wood-deep) 100%);
  }
  .front-brand {
    position: absolute; left: 50%; top: 50%; transform: translate(-50%, -50%);
    display: flex; align-items: center; gap: 22px;
  }
  .front-brand .dot { width: 64px; height: 64px; border-radius: 50%; background: var(--green); }
  .front-brand .name {
    font-family: "Montserrat", sans-serif; font-weight: 800; font-size: 64px;
    letter-spacing: 3px; color: var(--charcoal);
  }

  .card-back {
    position: absolute; left: 0; top: 613px; width: 1039px; height: 587px;
    background: var(--page); border: 1px solid var(--card-edge);
  }
  .back-brand {
    position: absolute; left: 92px; top: 248px;
    display: flex; align-items: center; gap: 14px;
  }
  .back-brand .dot { width: 34px; height: 34px; border-radius: 50%; background: var(--green); }
  .back-brand .name {
    font-family: "Montserrat", sans-serif; font-weight: 800; font-size: 36px;
    letter-spacing: 1.5px; color: var(--green);
  }
  .divider {
    position: absolute; left: 474px; top: 86px; width: 4px; height: 414px; background: var(--rule);
  }
  .holder-name {
    position: absolute; left: 528px; top: 131px;
    font-family: "Montserrat", sans-serif; font-weight: 800; font-size: 31px;
    letter-spacing: 2px; color: var(--green);
  }
  .holder-title {
    position: absolute; left: 529px; top: 172px;
    font-size: 23px; color: var(--grey-text); letter-spacing: .3px;
  }
  .contacts { position: absolute; left: 530px; top: 322px; list-style: none; }
  .contacts li { display: flex; align-items: center; height: 50px; margin-bottom: 2px; }
  .contacts svg { width: 42px; height: 42px; margin-right: 14px; flex: none; }
  .contacts span { font-size: 28px; color: var(--ink); letter-spacing: .4px; }
</style>
</head>
<body>
  <section class="card-front" role="img" aria-label="Light natural wood grain background">
    <div class="front-brand">
      <span class="dot"></span>
      <span class="name">VERDALUX</span>
    </div>
  </section>

  <section class="card-back">
    <div class="back-brand">
      <span class="dot"></span>
      <span class="name">VERDALUX</span>
    </div>

    <div class="divider"></div>

    <h1 class="holder-name">KARIM SAID NADER</h1>
    <p class="holder-title">Chief Executive Officer</p>

    <ul class="contacts">
      <li>
        <svg viewBox="0 0 42 42" aria-hidden="true">
          <rect x="9" y="1" width="24" height="40" rx="5" fill="var(--green)"/>
          <rect x="13" y="6" width="16" height="25" rx="1.5" fill="#fff"/>
          <circle cx="21" cy="36" r="2.4" fill="#fff"/>
        </svg>
        <span>009715 555 010 42</span>
      </li>
      <li>
        <svg viewBox="0 0 42 42" aria-hidden="true">
          <rect x="1" y="8" width="40" height="26" rx="3" fill="var(--green)"/>
          <path d="M4 11 L21 24 L38 11 M4 31 L16 20 M38 31 L26 20" stroke="#fff" stroke-width="2.6" fill="none" stroke-linejoin="round"/>
        </svg>
        <span>IT@VERDALUX.com</span>
      </li>
      <li>
        <svg viewBox="0 0 42 42" aria-hidden="true">
          <circle cx="21" cy="21" r="19" fill="var(--green)"/>
          <g stroke="#fff" stroke-width="2.4" fill="none">
            <circle cx="21" cy="21" r="12"/>
            <ellipse cx="21" cy="21" rx="5.5" ry="12"/>
            <line x1="9" y1="21" x2="33" y2="21"/>
          </g>
        </svg>
        <span>www.VERDALUX.ae</span>
      </li>
    </ul>
  </section>
</body>
</html>
```